Cause bitches need love too!

I am creating an ad campaign. It will be a series of featured dogs in our shelter and they will contain a picture of the dog wich should be big enough to see on a yard sign and will change every week. I am placing the signs so that they lead you to the shelter. This is why I am also including the copy that says "you're almost there".

I have 4 tag lines:

1. Find unconditional Love.
2. She'll Love you furever!
3. He'll always listen.
4. Meet your new BFF

You're almost there 318 W Harrowgate Ln
Open 10 - 7/Tues-Sat

The dimensions for the sign are 24" wide and 18" high

Every week we will have a different picture of a different dog (hopefully last week's dog gets adopted). Anyhow, I am printing out yard signs, meaning that instead of printing 160 different signs it would be ideal just to replace the photo. So far the copy that is permanent is: "You're almost there. 318 W. Harrowgate Ln."

I could silhouette the image of the dog as well and super impose it on the sign, that's also a consideration, but ideally if I could have 4 tag lines I could print 40 signs of each and just replace the photo manually each week from my printer that would save costs.
Updates

Not enough designs to chose from and I edited the brief and committed to pay no matter what to increase the amount of designs as per your suggestions.

Target Market(s)

Animal lovers

Industry/Entity Type

Campaign

Font styles to use
Sans Serif

Colors

Designer to choose colors to be used in the design.

Requirements
Must have
• The dimensions for the sign are 24" wide and 18" high
Nice to have
• I want the signs to be hip, they should have a positive feel to them. You can alter the photos if you like. I am even open to new copy if you think something else works better.

```html
<!DOCTYPE html>
<html lang="en">
<head>
<meta charset="utf-8">
<title>Find unconditional Love – Yard Sign</title>
<link rel="stylesheet" href="https://fonts.googleapis.com/css2?family=Cutive&family=Open+Sans:wght@400;600;700&display=swap">
<style>
  :root {
    --paper: #f3f4f5;
    --sage: #8aab9c;
    --sage-light: #a9c5b8;
    --rule-grey: #d9dbdc;
    --cocoa: #7a6357;
    --ink: #4a4b4d;
    --white: #ffffff;
    --photo-light: #b3aca6;
    --photo-mid: #8f857d;
    --photo-dark: #6e655f;
  }
  * { margin: 0; padding: 0; box-sizing: border-box; }
  html, body {
    width: 1200px;
    height: 894px;
    overflow: hidden;
    background: var(--paper);
  }
  .sign {
    position: relative;
    width: 1200px;
    height: 894px;
    background: var(--paper);
    overflow: hidden;
  }
  .sign__art {
    position: absolute;
    inset: 0;
    width: 1200px;
    height: 894px;
  }
  .tagline {
    position: absolute;
    left: 48px;
    top: 78px;
    font-family: "Cutive", "Courier New", serif;
    font-size: 66px;
    line-height: 100px;
    color: var(--cocoa);
    letter-spacing: -1px;
  }
  .tagline__rule {
    position: absolute;
    left: 46px;
    top: 379px;
    width: 358px;
    height: 2px;
    background: var(--sage);
  }
  .directions {
    position: absolute;
    left: 48px;
    top: 470px;
    font-family: "Open Sans", Arial, sans-serif;
    color: var(--ink);
  }
  .directions__lead {
    font-size: 33px;
    font-weight: 400;
    letter-spacing: 0.5px;
    text-transform: uppercase;
  }
  .directions__address {
    display: flex;
    align-items: center;
    gap: 24px;
    margin-top: 34px;
    font-size: 33px;
    font-weight: 700;
  }
  .directions__pin { width: 22px; height: 34px; flex: none; }
  .hours {
    position: absolute;
    left: 48px;
    top: 793px;
    font-family: "Open Sans", Arial, sans-serif;
    font-size: 34px;
    color: var(--white);
  }
</style>
</head>
<body>
<main class="sign">
  <svg class="sign__art" viewBox="0 0 1200 894" aria-hidden="false">
    <defs>
      <linearGradient id="dogPhotoTone" x1="0" y1="0" x2="1" y2="1">
        <stop offset="0" stop-color="var(--photo-light)"/>
        <stop offset="0.55" stop-color="var(--photo-mid)"/>
        <stop offset="1" stop-color="var(--photo-dark)"/>
      </linearGradient>
    </defs>

    <!-- bottom sage wave with thin grey line above -->
    <path class="wave-line" d="M0 697 Q200 664 600 716" fill="none" stroke="var(--rule-grey)" stroke-width="3"/>
    <path class="wave-band" d="M0 728 Q170 700 620 738 L620 894 L0 894 Z" fill="var(--sage)"/>

    <!-- faint paw print area -->
    <g role="img" aria-label="Faint paw print decoration">
      <ellipse cx="118" cy="680" rx="68" ry="62" fill="#dfe1e2" opacity="0.7"/>
    </g>

    <!-- sage arc band -->
    <path class="arc-band" d="M756 0 Q388 447 603 894 L1200 894 L1200 0 Z" fill="var(--sage-light)"/>
    <!-- white gap -->
    <path class="arc-gap" d="M790 0 Q420 447 628 894 L1200 894 L1200 0 Z" fill="var(--white)"/>
    <!-- featured dog photo -->
    <path class="dog-photo" role="img" aria-label="Photo of this week's featured shelter dog, a grey and white pit bull looking up"
          d="M815 0 Q454 447 653 894 L1200 894 L1200 0 Z" fill="url(#dogPhotoTone)"/>
  </svg>

  <h1 class="tagline">Find<br>unconditional<br>Love.</h1>
  <div class="tagline__rule"></div>

  <section class="directions">
    <p class="directions__lead">You're almost there</p>
    <p class="directions__address">
      <svg class="directions__pin" viewBox="0 0 22 34" aria-hidden="true">
        <path d="M11 0C4.9 0 0 4.9 0 11c0 8 11 23 11 23s11-15 11-23C22 4.9 17.1 0 11 0zm0 15.5a4.5 4.5 0 1 1 0-9 4.5 4.5 0 0 1 0 9z" fill="var(--ink)"/>
      </svg>
      318 W Harrowgate Ln
    </p>
  </section>

  <p class="hours">Open 10 - 7/Tues-Sat</p>
</main>
</body>
</html>
```